Design a Logo and business card for my real estate company

Harborline Properties- this is the company

Tom Kessler
Broker - Realtor - Investor
925-555-0147
BRE# 01072936

```html
<!DOCTYPE html>
<html lang="en">
<head>
<meta charset="utf-8">
<title>Harborline Properties – Business Card</title>
<link rel="stylesheet" href="https://fonts.googleapis.com/css2?family=Federo&family=Poppins:wght@400;600&display=swap">
<style>
  :root {
    --page-bg: #e9e8e6;
    --frame-blue: #2236d4;
    --frame-deep: #12209a;
    --panel-blue: #2a3ee0;
    --gold: #8c7a1c;
    --gold-line: #b59a3a;
    --name-blue: #1f31c4;
    --ink: #33405e;
    --frost-top: #f7f7f5;
    --frost-bottom: #e3e2e0;
  }
  * { margin: 0; padding: 0; box-sizing: border-box; }
  html, body {
    width: 1200px; height: 969px; overflow: hidden;
    background: var(--page-bg);
  }
  .canvas { position: relative; width: 1200px; height: 969px; }
  .card {
    position: absolute; left: 60px; top: 185px;
    width: 1080px; height: 600px;
    box-shadow: 0 14px 40px rgba(0,0,0,0.18);
  }
  .card-art { position: absolute; inset: 0; }
  .card-content { position: absolute; inset: 0; }

  .brand {
    position: absolute; left: 0; right: 0; top: 150px;
    display: flex; justify-content: center; align-items: center; gap: 18px;
  }
  .brand-mark { width: 26px; height: 26px; background: var(--gold); }
  .brand-name {
    font-family: "Poppins", sans-serif; font-weight: 600;
    font-size: 46px; letter-spacing: 2px; color: var(--gold);
    text-transform: uppercase;
  }
  .brand-rule {
    position: absolute; left: 228px; width: 606px; top: 243px;
    height: 4px; background: var(--name-blue);
  }
  .person-name {
    position: absolute; left: 0; right: 0; top: 305px; text-align: center;
    font-family: "Federo", sans-serif; font-size: 56px; letter-spacing: 3px;
    color: var(--name-blue); text-transform: uppercase;
  }
  .person-role {
    position: absolute; left: 0; right: 0; top: 378px; text-align: center;
    font-family: "Poppins", sans-serif; font-weight: 600; font-size: 25px;
    letter-spacing: 4px; color: var(--gold); text-transform: uppercase;
  }
  .contact-list {
    position: absolute; left: 296px; top: 446px; list-style: none;
    font-family: "Poppins", sans-serif; font-size: 28px; color: var(--ink);
  }
  .contact-list li { display: flex; align-items: center; gap: 10px; height: 39px; }
  .contact-icon { width: 24px; height: 24px; flex: none; }
  .url { text-transform: uppercase; letter-spacing: 0.5px; }
</style>
</head>
<body>
<div class="canvas">
  <div class="card">
    <svg class="card-art" viewBox="0 0 1080 600" width="1080" height="600">
      <defs>
        <linearGradient id="frost" x1="0" y1="0" x2="0" y2="1">
          <stop offset="0" stop-color="#f8f8f6"/>
          <stop offset="1" stop-color="#e2e1df"/>
        </linearGradient>
        <linearGradient id="frame" x1="0" y1="0" x2="0" y2="1">
          <stop offset="0" stop-color="#2a40e6"/>
          <stop offset="1" stop-color="#1a2bb8"/>
        </linearGradient>
      </defs>
      <rect class="frame" x="0" y="0" width="1080" height="600" fill="url(#frame)"/>
      <rect class="frame-inner-line" x="14" y="14" width="1052" height="572" fill="none" stroke="#12209a" stroke-width="3"/>
      <rect class="frost" x="22" y="22" width="1036" height="556" fill="url(#frost)"/>
      <path class="side-panel left" d="M22 22 H128 Q104 72 150 102 Q216 142 216 300 Q216 452 150 492 Q104 526 128 578 H22 Z"
            fill="#2a3ee0" stroke="#b59a3a" stroke-width="3"/>
      <path class="side-panel right" d="M1058 22 H952 Q976 72 930 102 Q864 142 864 300 Q864 452 930 492 Q976 526 952 578 H1058 Z"
            fill="#2a3ee0" stroke="#b59a3a" stroke-width="3"/>
    </svg>

    <div class="card-content">
      <div class="brand">
        <span class="brand-mark"></span>
        <span class="brand-name">Harborline Properties</span>
      </div>
      <div class="brand-rule"></div>
      <div class="person-name">Tom Kessler</div>
      <div class="person-role">Broker - Realtor - Investor</div>
      <ul class="contact-list">
        <li>
          <svg class="contact-icon" viewBox="0 0 24 24"><path d="M6 3 L9 3 L10.5 7.5 L8.5 9 Q10 13 15 15.5 L16.5 13.5 L21 15 L21 18 Q20 21 17 21 Q4 19 3 6 Q3 3 6 3 Z" fill="#8c7a1c"/></svg>
          <span>925-555-0147</span>
        </li>
        <li>
          <svg class="contact-icon" viewBox="0 0 24 24"><circle cx="12" cy="12" r="9" fill="none" stroke="#8c7a1c" stroke-width="2"/><ellipse cx="12" cy="12" rx="4" ry="9" fill="none" stroke="#8c7a1c" stroke-width="1.6"/><line x1="3" y1="12" x2="21" y2="12" stroke="#8c7a1c" stroke-width="1.6"/></svg>
          <span class="url">www.brightbayhomesteads.com</span>
        </li>
        <li>
          <svg class="contact-icon" viewBox="0 0 24 24"><path d="M12 2 C7.5 2 5 5.2 5 9 C5 14 12 22 12 22 C12 22 19 14 19 9 C19 5.2 16.5 2 12 2 Z" fill="#8c7a1c"/><circle cx="12" cy="9" r="2.6" fill="#f3f2f0"/></svg>
          <span>BRE# 01072936</span>
        </li>
      </ul>
    </div>
  </div>
</div>
</body>
</html>
```